Velmora - New coded website

Current website is around 5 years old and corrupted in some ways...
I would like to refresh the design and to create a new coded website based on the current content .
Please refer to :
www.velmora-sample.com.au

Coded - Design and coding required

```html
<!DOCTYPE html>
<html lang="en">
<head>
<meta charset="utf-8">
<title>Velmora | Odour Control Solution</title>
<link href="https://fonts.googleapis.com/css2?family=Inter:wght@400;500&family=Lobster&display=swap" rel="stylesheet">
<style>
  :root {
    --teal-dark: #055a73;
    --teal-brand: #0c5470;
    --leaf-green: #6cb33f;
    --nav-grey: #6b6b6b;
    --white: #ffffff;
    --ink: #111111;
  }
  * { box-sizing: border-box; margin: 0; padding: 0; }
  html, body {
    width: 1200px;
    height: 755px;
    overflow: hidden;
    background: var(--white);
    font-family: "Inter", Arial, sans-serif;
  }
  .site { width: 1200px; height: 755px; position: relative; overflow: hidden; }

  .topbar {
    height: 44px;
    background: var(--teal-dark);
    color: var(--white);
    font-size: 17px;
    font-weight: 500;
    display: flex;
    align-items: center;
    justify-content: space-between;
    padding: 0 40px 0 112px;
  }
  .topbar__item { display: flex; align-items: center; gap: 6px; white-space: nowrap; }
  .topbar__icon { width: 17px; height: 17px; fill: var(--white); }

  .header {
    height: 108px;
    display: flex;
    align-items: center;
    justify-content: space-between;
    padding: 0 40px 0 34px;
  }
  .brand { display: flex; align-items: center; gap: 14px; }
  .brand__dot {
    width: 84px; height: 84px; border-radius: 50%;
    background: var(--leaf-green);
  }
  .brand__name {
    font-size: 44px;
    font-weight: 400;
    color: var(--teal-brand);
    letter-spacing: -0.5px;
  }
  .nav { display: flex; align-items: center; gap: 17px; }
  .nav__link { font-size: 17px; color: var(--nav-grey); text-decoration: none; white-space: nowrap; }
  .nav__cta {
    margin-left: 5px;
    background: var(--teal-brand);
    color: var(--white);
    font-size: 17px;
    padding: 15px 22px;
    border-radius: 6px;
    white-space: nowrap;
  }

  .hero {
    position: relative;
    height: 553px;
    background:
      linear-gradient(180deg, rgba(30,36,50,0.55) 0%, rgba(40,45,55,0.35) 30%, rgba(20,30,15,0.25) 60%, rgba(15,25,10,0.45) 100%),
      linear-gradient(180deg, #4a4e5c 0%, #7c7c80 28%, #8b9a6a 45%, #6f8a3a 62%, #4f6e22 80%, #3d5a1a 100%);
    display: flex;
    flex-direction: column;
    align-items: center;
    justify-content: center;
  }
  .hero__title {
    font-family: "Lobster", "Brush Script MT", cursive;
    font-size: 70px;
    font-weight: 400;
    color: var(--white);
    margin-top: -25px;
    text-shadow: 0 2px 6px rgba(0,0,0,0.3);
  }
  .hero__button {
    margin-top: 46px;
    background: var(--white);
    color: var(--ink);
    font-size: 17px;
    padding: 13px 22px;
    border-radius: 5px;
  }
</style>
</head>
<body>
<div class="site">
  <div class="topbar">
    <div class="topbar__item">
      <svg class="topbar__icon" viewBox="0 0 24 24" aria-hidden="true"><path d="M2 5h20v2.2l-10 7-10-7z M2 9.6l10 7 10-7V19H2z"/></svg>
      <span>Email Us</span>
    </div>
    <div class="topbar__item">
      <svg class="topbar__icon" viewBox="0 0 24 24" aria-hidden="true"><path d="M2 5h20v2.2l-10 7-10-7z M2 9.6l10 7 10-7V19H2z"/></svg>
      <span>+61 (08) 5550 0147</span>
    </div>
  </div>

  <header class="header">
    <div class="brand">
      <div class="brand__dot"></div>
      <span class="brand__name">Velmora</span>
    </div>
    <nav class="nav">
      <a class="nav__link" href="#">Home</a>
      <a class="nav__link" href="#">About Us</a>
      <a class="nav__link" href="#">Projects</a>
      <a class="nav__link" href="#">Contact</a>
      <span class="nav__cta">Request a Quote</span>
    </nav>
  </header>

  <section class="hero" role="img" aria-label="Photograph of misty green rolling hills and pine forest at sunrise">
    <h1 class="hero__title">Odours Controlled Naturally</h1>
    <span class="hero__button">Request a Quote</span>
  </section>
</div>
</body>
</html>
```